Brochure for a website accessibility report

This brochure is related to a report that www.kelvat.org sell. The report shows the results of an automated audit of a websites accessibility. It shows details of issues found with screen shots, examples of code and provides remediation advice.

The brochure will be a pdf 8.5 inches by 11 inches. It can be anywhere from 6 to 10 pages.

The FaultLens™ name itself should be “Bree Serif” font. The fonts, styles, colors and sizes are up to you.

The images used and logo of the Office of Digital Openness and Q7N logo are upload

We highlighted in blue page extracts from the report we sell. Do not use the blue highlight, it is merely there to show you where the specific examples of the report we sell are vs the other content in the report. The areas in blue which show the content from the actual report should be shown as an extract of the actual page of the report. You have flexibility to change the layout and the way the content look.

The red square callouts over the blue content are callouts that describe the specific page extracts. We used it as a red callout only so that you would be able to see it. You should change the specific location, look and feel of the callout to be appropriate

Target Market(s)

Marketing and Technical people

Industry/Entity Type

Information Technology

Font styles to use
Sans Serif

Colors

Designer to choose colors to be used in the design.

Requirements
Should not have
• wheelchairs, images of blind people

```html
<!DOCTYPE html>
<html lang="en">
<head>
<meta charset="utf-8">
<title>FaultLens™ Report – Structure</title>
<link rel="stylesheet" href="https://fonts.googleapis.com/css2?family=Bree+Serif&family=Roboto:wght@400;500;700&family=Noto+Serif:wght@400&display=swap">
<style>
  :root {
    --page-bg: #f7f3ef;
    --card-bg: #fdf1e0;
    --green: #1aa36a;
    --green-dark: #1f5c3c;
    --text: #555555;
    --text-strong: #444444;
    --gold: #e3b97a;
    --bullet: #e8c58f;
    --white: #ffffff;
    --code-bg: #f8f4ef;
    --shot-top: #c9b98a;
    --shot-bottom: #1b2f4d;
  }
  * { box-sizing: border-box; margin: 0; padding: 0; }
  html, body { width: 927px; height: 1200px; overflow: hidden; background: var(--page-bg); }
  body { position: relative; font-family: "Roboto", sans-serif; color: var(--text); font-size: 16px; }

  .card {
    position: absolute; left: 52px; top: 52px; width: 824px; height: 1096px;
    background: var(--card-bg); border-radius: 42px;
    box-shadow: 0 2px 10px rgba(0,0,0,0.06);
  }
  .abs { position: absolute; }
  .section-title {
    left: 103px; top: 76px; font-family: "Bree Serif", serif; font-size: 33px;
    color: var(--green); font-weight: 400;
  }
  .intro { left: 103px; top: 134px; }
  .guidelines { left: 103px; top: 164px; width: 662px; list-style: none; line-height: 20px; }
  .guidelines li { position: relative; padding-left: 32px; margin-bottom: 10.5px; }
  .guidelines li::before {
    content: ""; position: absolute; left: 1px; top: 7px; width: 6px; height: 6px; background: var(--bullet);
  }
  .issue-title { left: 103px; top: 359px; font-weight: 700; color: var(--text-strong); }
  .issue-title span { color: var(--green); }
  .issue-body { left: 103px; top: 382px; width: 722px; line-height: 25.7px; text-align: justify; }
  .checkpoint { color: var(--gold); margin-left: 18px; }
  .advice-title { left: 103px; top: 532px; font-weight: 700; color: var(--text-strong); }
  .advice-body { left: 103px; top: 555px; width: 722px; line-height: 25.5px; text-align: justify; }
  .token { font-family: "Noto Serif", serif; color: var(--green); font-size: 14.5px; }
  .reading-title { left: 103px; top: 657px; font-weight: 700; color: var(--text-strong); }
  .reading-links { left: 153px; top: 677px; line-height: 20px; color: var(--gold); }

  .callout {
    background: var(--white); border-radius: 18px; font-size: 13.5px; letter-spacing: 0.4px;
    text-transform: uppercase; color: var(--text); line-height: 17px;
    box-shadow: 0 2px 8px rgba(0,0,0,0.08); display: flex; align-items: center;
  }
  .callout-checkpoint { left: 521px; top: 461px; width: 339px; height: 94px; padding-left: 32px; }
  .callout-screens { left: 368px; top: 642px; width: 492px; height: 92px; padding-left: 32px; }
  .tails { left: 0; top: 0; width: 927px; height: 1200px; pointer-events: none; }

  .example {
    left: 82px; top: 745px; width: 762px; height: 371px; background: var(--white); border-radius: 21px;
  }
  .example-head { left: 103px; top: 762px; color: var(--green-dark); }
  .example-head b { font-weight: 700; margin-right: 10px; }
  .specific-title { left: 104px; top: 805px; font-weight: 700; color: var(--text-strong); }
  .specific-body { left: 104px; top: 826px; width: 512px; line-height: 23px; }
  .code-title { left: 104px; top: 921px; font-weight: 700; color: var(--text-strong); }
  .code-box {
    left: 101px; top: 949px; width: 515px; height: 146px; background: var(--code-bg);
    padding: 7px 14px; font-family: "Noto Serif", serif; font-size: 11.8px; line-height: 16.2px;
    color: var(--green); text-transform: uppercase; text-align: justify;
    box-shadow: 0 1px 4px rgba(0,0,0,0.05); overflow: hidden;
  }
  .page-shot {
    left: 634px; top: 806px; width: 190px; height: 196px;
    background: linear-gradient(to bottom, var(--shot-top) 0 12%, #f4f4f4 12% 83%, var(--shot-bottom) 83% 100%);
    border: 1px solid #ccc;
  }
</style>
</head>
<body>
  <div class="card"></div>

  <h1 class="abs section-title">Structure</h1>
  <p class="abs intro">Ensure that your HTML layout structuring is necessary and informative.</p>
  <ul class="abs guidelines">
    <li>Use tables appropriately; layout tables should not use table grouping/organization tags but data/list-like content tables should use grouping tags.</li>
    <li>Frames should be properly organized, titled and identified. Aria Roles should be used where relevant.</li>
    <li>Layout or structural imagery must not have a title-attribute and should have an empty alt-attribute.</li>
    <li>Instructive content should be provided along with skip-links as necessary.</li>
  </ul>

  <h2 class="abs issue-title">ISSUE: <span>LAYOUT TABLE WITH SUMMARY (PRIORITY 4)</span></h2>
  <div class="abs issue-body">
    The summary attribute on a layout table should be empty. The purpose of a layout table is simply to control the placement of content; the table itself is transparent to the user. A summary attribute would break this transparency by calling attention to the table. A null summary (summary="") on layout tables is acceptable.<br>
    Issue is relevant to checkpoints: <span class="checkpoint">1.3.1 (A).</span>
  </div>

  <h3 class="abs advice-title">General Remediation Advice:</h3>
  <p class="abs advice-body">Remove the <span class="token">summary</span> attribute from tables used solely for layout. It should only be used for tables that present tabular data. In HTML 5, you can use the <span class="token">role</span> attribute on the <span class="token">TABLE</span> with a value of "presentation" to explicitly mark the table as being used for layout.</p>

  <h3 class="abs reading-title">Suggested Reading:</h3>
  <div class="abs reading-links">Adaptable<br>Info and Relationships</div>

  <div class="abs example"></div>
  <div class="abs example-head"><b>EXAMPLE 1 OF 6:</b> HTTP://WWW.CR-ORG.INT/ES/DOCS/CR/XCHGCR.SHTML</div>
  <h3 class="abs specific-title">SPECIFIC ISSUES:</h3>
  <p class="abs specific-body">Layout tables should not have a 'SUMMARY' attribute; or it should be an empty text value. &nbsp;<span class="token">&lt;TABLE&gt; Tag</span> &nbsp; found &nbsp;<span class="token">summary='La tabla debe ser leída por fila. Tiene tres filas, cada una representa u...</span></p>
  <h3 class="abs code-title">CODE SNIPPET</h3>
  <div class="abs code-box">&lt;table class="yrlist" summary="La tabla debe ser le&amp;#237;da por fila. Tiene tres filas, cada una representa una d&amp;#233;cada, la fila de arriba es de la d&amp;#233;cada actual. Los v&amp;#237;nculos de los a&amp;#241;os en cada celda de la tabla abrir&amp;#225;n una p&amp;#225;gina con la lista de cartas intercambiadas durante ese a&amp;#241;o en particular."&gt; &lt;tbody&gt;&lt;tr&gt; &lt;th colspan="11" class="tbltitle"&gt;Intercambio de cartas del Secretario General y el Presidente del Consejo de Coordinación&lt;/th&gt;</div>
  <div class="abs page-shot" role="img" aria-label="Screenshot of the audited web page with the offending layout table highlighted"></div>

  <div class="abs callout callout-checkpoint">Each issue is detailed with links<br>to the specific WCAG checkpoint</div>
  <div class="abs callout callout-screens">Appropriate screenshots with the issue highlighted<br>are shown where the issue resides on the webpage</div>

  <svg class="abs tails" viewBox="0 0 927 1200" aria-hidden="true">
    <polygon points="523,478 429,498 523,510" fill="#ffffff"/>
    <polygon points="791,732 816,806 812,732" fill="#ffffff"/>
  </svg>
</body>
</html>
```